Inspiring Fundraising Foundation Website to Provide Academic Scholarships

Hello, we are launching a foundation to provide academic scholarships to high school students for college. We'd like this to be an informational website with contact information. There will be a total of approximately 5-7 pages in all.
The color scheme will be purple and white, with a girly feel. I 've attached the logo for reference!

Reason: Extending deadline to go over revisions

Target Market(s)

high school students, college students

Industry/Entity Type

Education

Coding

Coded - Design and coding required

Number of Pages Required

5+ page

Font styles to use
Serif
Sans Serif
Script

Colors
6b449b
886aae
b7a5cd
e4daeb
ffffff
fdf9cf
fbf289

Requirements
Must have
• Purple, girly feel, to reflect the logo's style. Should be light-themed
Should not have
• No dark themes (aka heavy on black or dark colors)

```html
<!DOCTYPE html>
<html lang="en">
<head>
<meta charset="utf-8">
<title>Mission And Vision – Lorena Vasquez Foundation</title>
<link href="https://fonts.googleapis.com/css2?family=Lato:wght@400;700&family=Dancing+Script:wght@600&display=swap" rel="stylesheet">
<style>
  :root{
    --purple:#4b2272;
    --purple-dark:#3b1858;
    --ink:#222222;
    --text:#444444;
    --grey-circle:#e6e6e6;
    --footer:#222222;
    --white:#ffffff;
    --social-1:#3b5a9a;
    --social-2:#55acee;
    --social-3:#0e76a8;
    --social-4:#dd3127;
  }
  *{box-sizing:border-box;margin:0;padding:0}
  html,body{width:966px;height:1200px;overflow:hidden;background:var(--white)}
  body{position:relative;font-family:'Lato',sans-serif;color:var(--text)}
  .abs{position:absolute}

  /* header */
  .site-header{position:absolute;left:0;top:0;width:966px;height:137px;background:var(--white)}
  .brand{left:66px;top:40px;width:110px;font-size:17px;font-weight:700;line-height:20px;color:var(--purple)}
  .social-top{left:600px;top:29px;display:flex;gap:6px}
  .social-top span{display:block;width:33px;height:33px}
  .s-1{background:var(--social-1)}.s-2{background:var(--social-2)}.s-3{background:var(--social-3)}.s-4{background:var(--social-4)}
  .donate{left:765px;top:29px;width:135px;height:33px;background:var(--purple);color:var(--white);
    font-size:13.5px;font-weight:700;display:flex;align-items:center;justify-content:center;letter-spacing:.2px}
  .main-nav{left:268px;top:93px}
  .main-nav a{position:absolute;white-space:nowrap;font-size:13.5px;font-weight:700;color:var(--ink);text-decoration:none;top:0}
  .main-nav a.active{color:var(--purple)}
  .nav-underline{left:435px;top:118px;width:138px;height:2px;background:var(--purple)}

  /* hero */
  .hero{left:0;top:137px;width:966px;height:229px;
    background:linear-gradient(90deg,#5f6a66 0%,#8b8681 35%,#6d5f55 65%,#3f3a36 100%)}
  .hero h1{position:absolute;left:0;right:0;top:94px;text-align:center;font-family:'Dancing Script',cursive;
    font-weight:600;font-size:36px;color:var(--white)}

  /* intro */
  .intro{left:66px;top:404px;width:478px;font-size:12.8px;line-height:23.7px;color:var(--ink)}
  .points{left:66px;top:533px;list-style:none}
  .points li{position:relative;height:33.3px;padding-left:22px;font-size:11.5px;color:var(--text);line-height:18px}
  .points svg{position:absolute;left:0;top:3px}
  .intro-photo{left:558px;top:407px;width:344px;height:286px;
    background:linear-gradient(135deg,#b9c9a8 0%,#d9b8a0 45%,#3b4a66 75%,#c9c2b8 100%)}

  /* mission / vision */
  .pillar{top:735px;width:430px}
  .pillar .icon{position:absolute;left:0;top:0;width:72px;height:72px;border-radius:50%;background:var(--grey-circle);
    display:flex;align-items:center;justify-content:center}
  .pillar h2{position:absolute;left:89px;top:4px;font-size:18px;font-weight:700;color:var(--purple)}
  .pillar p{position:absolute;left:89px;top:31px;width:320px;font-size:11.5px;line-height:20.6px;color:var(--text)}
  .pillar.vision p{line-height:16.2px;width:322px}
  .mission{left:67px}
  .vision{left:494px}

  /* footer */
  .site-footer{left:0;top:926px;width:966px;height:231px;background:var(--footer);color:var(--white)}
  .f-col{top:36px}
  .f-col h3{font-size:13px;font-weight:700;letter-spacing:.1px}
  .f-col h3::after{content:"";display:block;width:30px;height:2px;background:var(--white);margin-top:8px}
  .quick{left:66px}
  .quick ul{list-style:none;margin-top:12px}
  .quick li{font-size:11.5px;height:20px;line-height:20px}
  .quick li::before{content:"›";margin-right:5px}
  .contact{left:240px}
  .contact .row{position:relative;padding-left:20px;font-size:10.5px;line-height:14px}
  .contact .row svg{position:absolute;left:0;top:1px}
  .contact strong{font-weight:700;font-size:11px}
  .map-col{left:506px}
  .map{margin-top:15px;width:188px;height:111px;border:2px solid #ddd;
    background:linear-gradient(135deg,#b8d3ee 0%,#e9e4d6 45%,#a9c8e6 100%)}
  .footer-brand{left:778px;top:92px;width:125px;font-size:17px;font-weight:700;line-height:20px;color:#d9d9d9;text-align:center}

  .bottom-bar{left:0;top:1157px;width:966px;height:43px;background:var(--purple-dark);color:var(--white)}
  .bottom-bar p{position:absolute;left:66px;top:13px;font-size:11.5px}
  .social-foot{position:absolute;left:772px;top:8px;display:flex;gap:8px}
  .social-foot span{width:26px;height:26px;border:1.5px solid var(--white);border-radius:50%}
</style>
</head>
<body>

<header class="site-header">
  <div class="abs brand">Lorena Vasquez Foundation</div>
  <div class="abs social-top" aria-label="Social links">
    <span class="s-1" aria-label="Social link 1"></span>
    <span class="s-2" aria-label="Social link 2"></span>
    <span class="s-3" aria-label="Social link 3"></span>
    <span class="s-4" aria-label="Social link 4"></span>
  </div>
  <a class="abs donate">DONATE NOW</a>
  <nav class="abs main-nav">
    <a style="left:0">HOME</a>
    <a style="left:71px">ABOUT US</a>
    <a class="active" style="left:167px">MISSION AND VISION</a>
    <a style="left:335px">EVENTS</a>
    <a style="left:416px">PRESS RELEASES</a>
    <a style="left:548px">CONTACT US</a>
  </nav>
  <div class="abs nav-underline"></div>
</header>

<section class="abs hero" role="img" aria-label="Photo of students smiling together in a classroom">
  <h1>Mission And Vision</h1>
</section>

<p class="abs intro">Lorem ipsum dolor sit amet, consectetur adipiscing elit. Etiam nec nibh at liberote volutpat porta et eu neque. Cum sociis natoque penatibus et magnis dis parturient montes, nascetur ridiculus mus. Nam feugiat ligula sed nibh pellentesque, acduiet pellentesque metus ultricies. Donec ac&nbsp; at mi consectetur viverra. Sedet euismod dui quis arcu pulvinar imperdiet duis tempor.</p>

<ul class="abs points">
  <li><svg width="15" height="12" viewBox="0 0 15 12"><path d="M1 5h9M7 2l4 3-4 3" fill="none" stroke="#333" stroke-width="1.4"/></svg>Aliquam laoreet porta tortor eu semper quisque sagittis quam id orn.</li>
  <li><svg width="15" height="12" viewBox="0 0 15 12"><path d="M1 5h9M7 2l4 3-4 3" fill="none" stroke="#333" stroke-width="1.4"/></svg>Aenean non pellentesque mauris aliquam urna sit amet neq.</li>
  <li><svg width="15" height="12" viewBox="0 0 15 12"><path d="M1 5h9M7 2l4 3-4 3" fill="none" stroke="#333" stroke-width="1.4"/></svg>Donec ac&nbsp; at mi consectetur viverra sedet euismod du.</li>
  <li><svg width="15" height="12" viewBox="0 0 15 12"><path d="M1 5h9M7 2l4 3-4 3" fill="none" stroke="#333" stroke-width="1.4"/></svg>Aliquam laoreet porta tortor eu semper quisque sagittis quam id orn.</li>
  <li><svg width="15" height="12" viewBox="0 0 15 12"><path d="M1 5h9M7 2l4 3-4 3" fill="none" stroke="#333" stroke-width="1.4"/></svg>Donec ac&nbsp; at mi consectetur viverra sedet euismod du.</li>
</ul>

<div class="abs intro-photo" role="img" aria-label="Photo of four students laughing around a laptop outdoors"></div>

<section class="abs pillar mission">
  <div class="icon">
    <svg width="40" height="40" viewBox="0 0 40 40" fill="none" stroke="#4b2272" stroke-width="3.5">
      <circle cx="19" cy="21" r="15"/><circle cx="19" cy="21" r="8.5"/><circle cx="19" cy="21" r="2.5" fill="#4b2272"/>
      <path d="M19 21L35 5M30 4h5v5" stroke-width="3"/>
    </svg>
  </div>
  <h2>Mission</h2>
  <p>Sed ut perspiciatis unde omnis iste natus error sit voluptatem accusantium doloremque laudantium, totam remrete aperiam, eaque ipsa quae ab illo inventore veritatis et quasie architecto beatae vitae dicta sunt explicabo. Nemo enim ipsam voluptate quia voluptas sit aspernatur aut odit aut fugiteti consequuntur magni dolores eos qui ratione voluptatem sequi nesciunt.</p>
</section>

<section class="abs pillar vision">
  <div class="icon">
    <svg width="46" height="28" viewBox="0 0 46 28">
      <path d="M2 14C10 3 36 3 44 14C36 25 10 25 2 14Z" fill="#4b2272"/>
      <circle cx="23" cy="14" r="8" fill="#e6e6e6"/><circle cx="23" cy="14" r="4.5" fill="#4b2272"/>
    </svg>
  </div>
  <h2>Vision</h2>
  <p>Sed ut perspiciatis unde omnis iste natus error sit voluptatem accusantium doloremque laudantium, totam remrete aperiam, eaque ipsa quae ab illo inventore veritatis et quasie architecto beatae vitae dicta sunt explicabo. Nemo enim ipsam voluptate quia voluptas sit aspernatur aut odit aut fugiteti consequuntur magni dolores eos qui ratione voluptatem sequi nesciunt.</p>
</section>

<footer class="abs site-footer">
  <div class="abs f-col quick">
    <h3>QUICK LINKS</h3>
    <ul>
      <li>Home</li><li>About Us</li><li>Mission And Vision</li><li>Events</li><li>Press Releases</li><li>Contact Us</li>
    </ul>
  </div>
  <div class="abs f-col contact">
    <h3>CONTACT DETAILS</h3>
    <div class="row" style="margin-top:14px">
      <svg width="12" height="16" viewBox="0 0 12 16"><path d="M6 0a6 6 0 0 1 6 6c0 4-6 10-6 10S0 10 0 6a6 6 0 0 1 6-6z" fill="#ccc"/><circle cx="6" cy="6" r="2.2" fill="#222"/></svg>
      <strong>Lorena Vasquez Foundation</strong><br>123 PG Duis aute irur dolore<br>srephenderit amit in voluptate
    </div>
    <div class="row" style="margin-top:12px;font-weight:700;font-size:11px">
      <svg width="12" height="13" viewBox="0 0 12 13"><path d="M2 1l3 3-1.5 1.5c1 2 2 3 4 4L9 8l3 3-2 2C5 12 0 7 0 3z" fill="#ccc"/></svg>
      + (123) 456 7890
    </div>
    <div class="row" style="margin-top:13px;font-weight:700;font-size:11px">
      <svg width="13" height="13" viewBox="0 0 13 13"><rect x="3" y="0" width="7" height="4" fill="#ccc"/><rect x="0" y="4" width="13" height="6" fill="#ccc"/><rect x="3" y="8" width="7" height="5" fill="#fff" stroke="#ccc"/></svg>
      + (123) 456 7890
    </div>
    <div class="row" style="margin-top:13px">
      <svg width="13" height="10" viewBox="0 0 13 10"><rect width="13" height="10" fill="#ccc"/><path d="M0 0l6.5 5L13 0" fill="none" stroke="#222"/></svg>
      info@lorenavasquezfoundation.org
    </div>
  </div>
  <div class="abs f-col map-col">
    <h3>LOCATION MAP</h3>
    <div class="map" role="img" aria-label="Street map showing the foundation's location"></div>
  </div>
  <div class="abs footer-brand">Lorena Vasquez Foundation</div>
</footer>

<div class="abs bottom-bar">
  <p>Copyright © 2016 Lorena Vasquez Foundation.&nbsp; All Rights Reserved.</p>
  <div class="social-foot" aria-label="Social links">
    <span aria-label="Social link 1"></span><span aria-label="Social link 2"></span><span aria-label="Social link 3"></span><span aria-label="Social link 4"></span>
  </div>
</div>

</body>
</html>
```